Brightwell Business Courses by Corvani LLC

Need source code for this app with one lesson examples copied. The app should include the copied content from Chapter 1 of "Accounting: Ledger Balance Drills" which in turn consists of 4 sub-chapters.
In addition, the app must contain copy of UI and code elements such that additional sub-chapters, additional chapters, and additional lessons can be added.

Requirements
Must have
• Source code for app must target IOS. Look and feel of the app can be identical to the reference app, Brightwell.
• No reference code available.
• The content of the lessons will be replaced with non-finance related material for internal training use.
Nice to have
• Mechanism for tracking progress for single user.
• Top level code in Swift.
• Web page implementations of Chapter 1.

```html
<!DOCTYPE html>
<html lang="en">
<head>
<meta charset="utf-8">
<title>Time Value Of Money — Chapter 1</title>
<link rel="stylesheet" href="https://fonts.googleapis.com/css2?family=Saira+Semi+Condensed:wght@400;500;700;800&family=Saira:wght@400;700;800&display=swap">
<style>
  :root {
    --teal: #009aab;
    --title-yellow: #f4ff00;
    --text-white: #f7fbfc;
  }
  * { margin: 0; padding: 0; box-sizing: border-box; }
  html, body {
    width: 846px;
    height: 1200px;
    overflow: hidden;
    background: var(--teal);
  }
  .lesson-page {
    position: relative;
    width: 846px;
    height: 1200px;
    background: var(--teal);
    color: var(--text-white);
  }
  .lesson-title {
    position: absolute;
    left: 64px;
    top: 106px;
    font-family: "Saira", sans-serif;
    font-weight: 800;
    font-size: 54px;
    line-height: 62px;
    letter-spacing: -0.5px;
    white-space: nowrap;
    color: var(--title-yellow);
  }
  .chapter-label {
    position: absolute;
    left: 64px;
    top: 288px;
    font-family: "Saira", sans-serif;
    font-weight: 700;
    font-size: 37px;
    line-height: 44px;
    white-space: nowrap;
  }
  .section-heading {
    position: absolute;
    left: 64px;
    font-family: "Saira", sans-serif;
    font-weight: 700;
    font-size: 29px;
    line-height: 34px;
    letter-spacing: 0.6px;
    white-space: nowrap;
  }
  .section-body {
    position: absolute;
    left: 64px;
    width: 740px;
    font-family: "Saira Semi Condensed", "Saira", sans-serif;
    font-weight: 400;
    font-size: 23.5px;
    line-height: 32px;
    white-space: nowrap;
  }
  .simple-heading { top: 411px; }
  .simple-body { top: 479px; }
  .compound-heading { top: 641px; }
  .compound-body { top: 708px; }
  .formula-heading { top: 904px; }
  .formula-body { top: 970px; }
</style>
</head>
<body>
  <main class="lesson-page">
    <h1 class="lesson-title">Time Value Of Money</h1>
    <h2 class="chapter-label">Chapter 1</h2>

    <h3 class="section-heading simple-heading">Simple Interest</h3>
    <p class="section-body simple-body">Simple interest is a topic that most people cover in elementary<br>school. Interest may be thought of as rent paid on borrowed money.<br>Simple interest is calculated only on the beginning principal.</p>

    <h3 class="section-heading compound-heading">Compound Interest</h3>
    <p class="section-body compound-body">Compound interest is another matter. It´s good to receive<br>compound interest, but not so good to pay compound interest. With<br>compound interest, interest is calculated not only on the beginning<br>interest,but on any interest accumulated in the meantime.</p>

    <h3 class="section-heading formula-heading">Compound Interest Formula</h3>
    <p class="section-body formula-body">Instead of calculating interest year-by-year, it would be simple to<br>see the future value of an investment using a compound interest<br>formula.</p>
  </main>
</body>
</html>
```